2-Sided Flyer for Printing - Quarvelent

We are looking for the most attractive and best quality flyer to serve as a handout to distribute as a printed document in fairs and conventions. We want one A4 sheet using two sides to display what is Quarvelent in an attractive and simple way.
• What is Quarvelent, what we do and benefits
o Type of challenges we solve
o Benefit for the companies
o Benefit for the solvers (engineers)
• How does it work
• Sample challenges
• Show our Community (skills, solvers pictures, etc)
The flyer should be developed according to our corporate colours (see landing page and logo)
The material we are uploading is the following:
• Power point with the introduction to Quarvelent
• Sample non professional flyers
• In addition you can use any material available through our web: www.quarvelent-example.com (landing page, blog, clients pages, ranking, etc.)

Target Market(s)

industrial companies and engineers

Industry/Entity Type

Engineering

Requirements
Must have
• A single flyer to be used for companies (clients) and engineers (solvers)
• overall flyer creative design
• clear and clean messages
• contain what is Quarvelent, how it works, community and sample challenges
• social networks info
• corporate pallet
Nice to have
• attractive funnel design to show how to move from a challenge to unique solutions
• attractive way to show the crowd using real solvers pictures
• Not all the background should be coloured (combination of white and corporate colours)
Should not have
• Copy and paste of the provided information and pictures
• High density content
• We do not like the design of the file "Brochure OK final.pdf" and we are looking for a 2-sided flyer

```html
<!DOCTYPE html>
<html lang="en">
<head>
<meta charset="utf-8">
<title>Quarvelent Flyer</title>
<link rel="stylesheet" href="https://fonts.googleapis.com/css2?family=Poppins:wght@400;500;600;700&display=swap">
<style>
  :root {
    --teal: #1ba597;
    --orange: #e8501c;
    --lime: #cdd500;
    --sky: #2eaae2;
    --mist: #e8eff6;
    --slate: #3b6676;
    --white: #ffffff;
    --ink: #454545;
  }
  * { box-sizing: border-box; margin: 0; padding: 0; }
  html, body { width: 1152px; height: 1200px; overflow: hidden; background: var(--white); }
  body { font-family: "Poppins", sans-serif; }
  .flyer { position: relative; width: 1152px; height: 1200px; overflow: hidden; }

  .hero { position: absolute; left: 0; top: 0; width: 1152px; height: 348px; background: var(--teal); color: var(--white); }
  .hero-title { position: absolute; left: 51px; top: 26px; font-size: 46px; font-weight: 600; line-height: 1.22; letter-spacing: 0.5px; }
  .hero-copy { position: absolute; left: 57px; width: 680px; font-size: 21px; line-height: 32px; font-weight: 400; }
  .hero-copy.first { top: 170px; }
  .hero-copy.second { top: 254px; }

  .brand-card { position: absolute; left: 765px; top: 0; width: 365px; height: 263px; background: var(--white); border-radius: 0 0 12px 12px; display: flex; align-items: center; justify-content: center; padding-top: 60px; }
  .brand-name { font-size: 50px; font-weight: 400; color: var(--ink); letter-spacing: 1px; }

  .section-band { position: absolute; left: 0; top: 348px; width: 1152px; height: 113px; background: var(--orange); display: flex; align-items: center; justify-content: center; }
  .section-title { color: var(--white); font-size: 55px; font-weight: 700; letter-spacing: 0.5px; }

  .features { position: absolute; left: 0; top: 461px; width: 1152px; height: 700px; background: var(--mist); }
  .features-backdrop { position: absolute; inset: 0; background: linear-gradient(120deg, #efe3e8 0%, #e3ebf2 35%, #e6efe0 60%, #dce9f3 100%); opacity: 0.8; }
  .features-shapes { position: absolute; left: 0; top: 0; }

  .feature { position: absolute; width: 310px; text-align: center; color: var(--white); }
  .feature-title { font-size: 32px; font-weight: 500; margin-bottom: 14px; white-space: nowrap; }
  .feature-copy { font-size: 21.5px; line-height: 36px; font-weight: 400; }
  .feature.lime { left: 444px; top: 146px; }
  .feature.orange { left: 96px; top: 320px; }
  .feature.sky { left: 772px; top: 331px; }

  .footer-band { position: absolute; left: 0; top: 1161px; width: 1152px; height: 39px; background: var(--slate); }
</style>
</head>
<body>
<main class="flyer">
  <header class="hero">
    <h1 class="hero-title">Turn Innovation into<br>Tangible Results</h1>
    <p class="hero-copy first">Quarvelent connects industrial companies with a global crowd of engineers to solve real technical challenges fast.</p>
    <p class="hero-copy second">Post your challenge, receive unique solutions from expert solvers and reward only the ideas that work.</p>
    <div class="brand-card"><span class="brand-name">Quarvelent</span></div>
  </header>

  <div class="section-band"><h2 class="section-title">WHAT CAN YOU EXPECT FROM US</h2></div>

  <section class="features">
    <div class="features-backdrop" role="img" aria-label="Soft background of faint pastel tiles"></div>
    <svg class="features-shapes" width="1152" height="700" viewBox="0 318 794 482" preserveAspectRatio="none" aria-hidden="true">
      <polygon fill="var(--lime)" points="292,357 498,358 560,492 492,632 302,632 255,490"/>
      <polygon fill="var(--orange)" points="95,479 268,479 310,610 260,757 92,753 22,605"/>
      <polygon fill="var(--sky)" points="555,480 718,482 788,612 718,757 540,752 490,612"/>
    </svg>

    <article class="feature lime">
      <h3 class="feature-title">How It Works</h3>
      <p class="feature-copy">Define your challenge, open it to our crowd, compare the ideas and pick the winner.</p>
    </article>
    <article class="feature orange">
      <h3 class="feature-title">For Companies</h3>
      <p class="feature-copy">Fresh expert ideas, lower R&amp;D costs and proven answers delivered in weeks.</p>
    </article>
    <article class="feature sky">
      <h3 class="feature-title">For Engineers</h3>
      <p class="feature-copy">Solve real industry problems, earn cash prizes and grow your global reputation.</p>
    </article>
  </section>

  <footer class="footer-band"></footer>
</main>
</body>
</html>
```